Vodka label, brand name: LATE BIRCH

We are looking for a vodka label design, which will print on paper or plastic (not a bottle printing)

We are small distilling company: Ferncliff Distillery. Located in Toronto, Canada. Our business is small batches of handcrafted very smooth vodka production. 40% abv. Made from cane sugar and spring water.

Our audience pretty mach everyone who consume vodka/alcohol, we are not targeting any specific group.

Back label should have barcode, government warning and this text:

Our vodka is handmade in small batches to the highest standards befitting the true vodka perfectionist. We use silk filtering process for exceptional purity, clarity, and smoothness. It is distilled 6 times from the finest organic cane sugar using only the best Canadian spring water. Discover the smooth, clear taste for yourself.
Distilled and Bottled by
Ferncliff Distillery Inc.
Toronto, Canada

Government Warning: In accordance to the Surgeon General, women should not drink alcoholic beverages during pregnancy because of the risk of birth defects. Consumption of alcoholic beverages impairs your ability to drive a car or operate machinery and may cause health problems.

Size of the bottle as follows (see example in the attachment) :
Volume: 750ml
Total height: 330mm
Body diameter: 77mm
Closure: Bar Top
Silver synthetic cork

Target Market(s)

Colors

Designer to choose colors to be used in the design.

Requirements
Must have
• Incorporate the name: LATE BIRCH
• Incorporate: DISTILLED FROM ORGANIC CANE SUGAR
• Back bottle label should have barcode, government warning and this text:
• Our vodka is handmade in small batches to the highest standards befitting the true vodka perfectionist. We use silk filtering process for exceptional purity, clarity, and smoothness. It is distilled 6 times from the finest organic cane sugar using only the best Canadian spring water. Discover the smooth, clear taste for yourself.
• Distilled and Bottleb by
• Ferncliff Distillery Inc.
• Toronto, Canada
• Government Warning: In accordance to the Surgeon General, women should not drink alcoholic beverages during pregnancy because of the risk of birth defects. Consumption of alcoholic beverages impairs your ability to drive a car or operate machinery and may cause health problems.
Nice to have
• 1) To show in wording or design it was Handmade
• 2) To show in wording or design it was made with Natural Spring Water
• To show in wording or design it was made in small batches
• 3) To show in wording or design it was made local in Toronto, Canada
• "The Six" "The 6ix"- is the nick name of city of Toronto that's just for designer to consider and not mandatory to implement on design
Should not have
• We try to lower cost of printing , so design should be for digital printing without Gold, Silver or any other color which requires foil application on label and will increase cost of printing.
• No copy paste from internet images. Such designs will be ignored and reported to website admin. Authentic design work only.
• Please try not to use clock or any related to that images. Its nothing to do with clock, its too naive to show 6 pm on the watches in your design. Its could be time of the day (evening), after work, the six as nick name of Toronto. But not clock or watches .

```html
<!DOCTYPE html>
<html lang="en">
<head>
<meta charset="utf-8">
<title>LATE BIRCH Hand-Crafted Vodka Label</title>
<link rel="stylesheet" href="https://fonts.googleapis.com/css2?family=Jost:wght@400;500&family=Montserrat:wght@700&family=Oswald:wght@500&display=swap">
<style>
  :root {
    --page-bg: #e9e9e9;
    --ink: #141414;
    --label-light: #f1f0ec;
    --label-mid: #d9d8d0;
    --label-edge: #bdbcb3;
    --neck-band: #3a3a38;
    --neck-text: #c9c9c4;
    --rule: #8e8d86;
  }
  * { margin: 0; padding: 0; box-sizing: border-box; }
  html, body {
    width: 810px;
    height: 1200px;
    overflow: hidden;
    background: var(--page-bg);
  }
  .canvas {
    position: relative;
    width: 810px;
    height: 1200px;
    display: flex;
    flex-direction: column;
    align-items: center;
  }

  /* Neck strip */
  .neck-label {
    margin-top: 70px;
    width: 64px;
    height: 340px;
    background: var(--neck-band);
    border: 2px solid #2a2a29;
    outline: 1px solid #6a6a66;
    outline-offset: -7px;
    display: flex;
    align-items: center;
    justify-content: center;
  }
  .neck-label__text {
    transform: rotate(-90deg);
    white-space: nowrap;
    display: flex;
    flex-direction: column;
    align-items: flex-start;
    color: var(--neck-text);
  }
  .neck-label__kicker {
    font: 400 9px/1 "Jost", sans-serif;
    letter-spacing: 0.08em;
    margin-bottom: 3px;
  }
  .neck-label__title {
    font: 700 27px/1 "Montserrat", sans-serif;
    letter-spacing: 0.1em;
  }

  /* Front label */
  .front-label {
    margin-top: 50px;
    width: 620px;
    height: 600px;
    background: linear-gradient(90deg, var(--label-edge) 0%, var(--label-mid) 14%, var(--label-light) 50%, var(--label-mid) 86%, var(--label-edge) 100%);
    color: var(--ink);
    display: flex;
    flex-direction: column;
    align-items: center;
    padding-top: 40px;
    text-align: center;
  }
  .front-label__claims {
    font: 400 19px/1.35 "Jost", sans-serif;
    letter-spacing: 0.03em;
  }
  .brand-name {
    margin-top: 58px;
    height: 170px;
    display: flex;
    align-items: center;
    gap: 18px;
    font: 500 52px/1 "Jost", sans-serif;
    letter-spacing: 0.12em;
  }
  .brand-name__dot {
    width: 22px;
    height: 22px;
    border-radius: 50%;
    background: var(--ink);
  }
  .front-label__style {
    margin-top: 30px;
    font: 400 22px/1 "Jost", sans-serif;
    letter-spacing: 0.04em;
  }
  .front-label__product {
    margin-top: 8px;
    font: 700 76px/1 "Montserrat", sans-serif;
    letter-spacing: 0.09em;
  }
  .front-label__source {
    margin-top: 26px;
    font: 400 17px/1 "Jost", sans-serif;
    letter-spacing: 0.04em;
  }
  .front-label__origin {
    margin-top: 20px;
    width: 440px;
    padding-bottom: 10px;
    border-bottom: 1px solid var(--rule);
    font: 500 21px/1 "Jost", sans-serif;
    letter-spacing: 0.08em;
  }
  .spec-row {
    margin-top: 22px;
    display: flex;
    align-items: center;
    font: 500 22px/1 "Oswald", sans-serif;
  }
  .spec-row__item { padding: 0 22px; }
  .spec-row__item small { font-size: 14px; }
  .spec-row__divider {
    width: 1.5px;
    height: 44px;
    background: var(--ink);
  }
</style>
</head>
<body>
  <main class="canvas">
    <div class="neck-label">
      <div class="neck-label__text">
        <span class="neck-label__kicker">HAND-CRAFTED</span>
        <span class="neck-label__title">VODKA</span>
      </div>
    </div>

    <section class="front-label">
      <p class="front-label__claims">MADE WITH NATURAL SPRING WATER<br>SMALL BATCH</p>
      <div class="brand-name">
        <span class="brand-name__dot"></span>
        <span>LATE BIRCH</span>
      </div>
      <p class="front-label__style">HAND-CRAFTED</p>
      <h1 class="front-label__product">VODKA</h1>
      <p class="front-label__source">DISTILLED FROM ORGANIC CANE SUGAR</p>
      <p class="front-label__origin">MADE IN TORONTO - CANADA</p>
      <div class="spec-row">
        <span class="spec-row__item">40% <small>Alc/Vol</small></span>
        <span class="spec-row__divider"></span>
        <span class="spec-row__item">80PROOF</span>
        <span class="spec-row__divider"></span>
        <span class="spec-row__item">750ml</span>
      </div>
    </section>
  </main>
</body>
</html>
```